Tidy Tuition Brochure

We offer payment processing and customer service solutions for the parents of Charter schools in the United States.
(More info: http://en.refvaultia.org/wiki/Charter_schools_in_the_United_States )

We have some content and are looking to make an 11x17 back and front design collateral piece. We are also looking for business cards and a 10'x10' trade show booth - separate projects but we can probably use the same designer across both.

Target Market(s)

School Administrators, people who work in school offices, specifically people who work with quickbooks or accounting software for schools.

Industry/Entity Type

Trade

Colors

Designer to choose colors to be used in the design.

Requirements
Must have
• Must have 2-4 pages, maybe 8 pages 1/2 size. It must use most of the content I included.
Nice to have
• I would like photos included - but realize that may not be possible given the space requirement.
Should not have
• Too many fonts, anything that is too glitzy.

```html
<!DOCTYPE html>
<html lang="en">
<head>
<meta charset="utf-8">
<title>Tidy Tuition – What Types of Payments</title>
<link rel="stylesheet" href="https://fonts.googleapis.com/css2?family=Barlow+Condensed:wght@400;500&family=Crimson+Pro:wght@400&display=swap">
<style>
  :root {
    --page-bg: #ffffff;
    --title-blue: #1d5cae;
    --body-ink: #1f1f1f;
    --rule-grey: #b9b9b9;
    --photo-teal: #4f8c86;
    --photo-teal-dark: #2f6660;
    --photo-cream: #d9cfc0;
  }
  * { margin: 0; padding: 0; box-sizing: border-box; }
  html, body {
    width: 927px;
    height: 1200px;
    overflow: hidden;
    background: var(--page-bg);
  }
  .brochure-page {
    position: relative;
    width: 927px;
    height: 1200px;
    background: var(--page-bg);
  }
  .section-title {
    position: absolute;
    top: 184px;
    left: 0;
    width: 927px;
    text-align: center;
    font-family: "Barlow Condensed", "Arial Narrow", sans-serif;
    font-weight: 400;
    font-size: 56px;
    line-height: 60px;
    color: var(--title-blue);
    letter-spacing: 0.5px;
  }
  .staff-photo {
    position: absolute;
    left: 55px;
    top: 279px;
    width: 396px;
    height: 710px;
    background:
      radial-gradient(ellipse at 55% 60%, var(--photo-cream) 0%, rgba(217,207,192,0.4) 30%, rgba(79,140,134,0) 55%),
      linear-gradient(160deg, var(--photo-teal) 0%, var(--photo-teal-dark) 100%);
  }
  .payment-list {
    position: absolute;
    left: 479px;
    top: 271px;
    width: 393px;
    list-style: none;
    font-family: "Crimson Pro", Georgia, serif;
    font-size: 18.5px;
    color: var(--body-ink);
  }
  .payment-item {
    height: 32.5px;
    padding-top: 5px;
    line-height: 25px;
    border-bottom: 1px solid var(--rule-grey);
    white-space: nowrap;
  }
  .payment-item:first-child { height: 32px; }
  .payment-item--two-line { height: 58.5px; }
</style>
</head>
<body>
  <main class="brochure-page">
    <h1 class="section-title">WHAT TYPES OF PAYMENTS:</h1>

    <div class="staff-photo" role="img" aria-label="Photo of a smiling school staff member in front of a classroom chalkboard"></div>

    <ul class="payment-list">
      <li class="payment-item">Payments for Damages/Repairs</li>
      <li class="payment-item">Payments for Goods/Services</li>
      <li class="payment-item payment-item--two-line">Payments for Extracurricular/<br>Non-Curricular Activities</li>
      <li class="payment-item payment-item--two-line">Payments for Activities that Supplement<br>a Class/Educational Program</li>
      <li class="payment-item payment-item--two-line">Payments for Uniforms/<br>Personal Athletic Equipment</li>
      <li class="payment-item">Payments for Registration / Security Deposits</li>
      <li class="payment-item">Payments for Extended Care Hours / Late Pickups</li>
      <li class="payment-item">Payments for Supplemental Field Trips</li>
      <li class="payment-item">Payments for Voluntary Student Insurance</li>
      <li class="payment-item payment-item--two-line">Payments for Technology Equipment /<br>Musical Instruments</li>
      <li class="payment-item">Payments for Lab and Shop Classes</li>
      <li class="payment-item">Payments for Student Publications</li>
      <li class="payment-item">Payments for Graduation Announcements</li>
      <li class="payment-item">Payments for Class Rings</li>
      <li class="payment-item">Payments for Post-Secondary Instructional Programs</li>
      <li class="payment-item payment-item--two-line">Payments for Lost and Destroyed Textbooks/<br>Workbooks/Library Books</li>
      <li class="payment-item">Payments for Voluntary Student Insurance</li>
      <li class="payment-item">Payments for Donations / Gifts</li>
    </ul>
  </main>
</body>
</html>
```